indépendant en tant que Massothérapeute et Préparateur Mental, j'ai besoin de ...

Massothérapeute et préparateur mental indépendant, je recherche une carte de visite sobre et dynamique, sans images liées au massage ou à la préparation mentale mais intégrant mon logo. Les couleurs que j'aime bien sont : Blanc, gris, anthracite, noir et jaune

Contact Information for Business Card

carte de préférence Horizontale
neutre qui puisse toucher le deux domaines Massothérapie et préparation mentale

Requirements
Must have
• mon projet doit intégrer au recto:
LOGO
Loïc Vermande
078 315 26 49
info@loicvermande-exemple.ch
et éventuellement www.loicvermande-exemple.ch

et au verso les deux adresses:

Chemin des Ormelets 27B
1400 Yverdon-les-Bains

Rue des Tanneries 9
1700 Fribourg

Should not have
• mon projet ne doit pas contenir d'image en liens avec le massage ni la préparation mentale.

```html
<!DOCTYPE html>
<html lang="fr">
<head>
<meta charset="UTF-8">
<title>Loïc Vermande – Carte de visite</title>
<link href="https://fonts.googleapis.com/css2?family=Poppins:wght@400;500;600&display=swap" rel="stylesheet">
<style>
  :root {
    --backdrop: #e4e5e7;
    --anthracite: #27313a;
    --paper: #ffffff;
    --ink: #1d1d1f;
    --ink-soft: #3a3a3c;
    --on-dark: #ffffff;
    --on-dark-soft: #d9dee2;
  }
  * { box-sizing: border-box; margin: 0; padding: 0; }
  html, body {
    width: 1200px; height: 900px; overflow: hidden;
    background: var(--backdrop);
    font-family: "Poppins", sans-serif;
  }
  .sheet {
    position: relative; width: 1200px; height: 900px;
  }
  .card {
    position: absolute; left: 290px; width: 620px; height: 380px;
    border-radius: 26px; overflow: hidden;
    box-shadow: 0 10px 30px rgba(0,0,0,.18);
  }
  .card--back { top: 45px; background: var(--anthracite); color: var(--on-dark); }
  .card--front { top: 475px; background: var(--paper); color: var(--ink); }

  .lockup { position: absolute; display: flex; align-items: center; gap: 16px; }
  .lockup__dot { width: 46px; height: 46px; border-radius: 50%; flex: none; }
  .card--back .lockup__dot { background: var(--on-dark); }
  .card--front .lockup__dot { background: var(--ink); }
  .lockup__name { font-size: 34px; font-weight: 600; line-height: 1; letter-spacing: .5px; }
  .lockup__role {
    margin-top: 6px; font-size: 10.5px; font-weight: 500;
    letter-spacing: 1.6px; text-transform: uppercase;
  }
  .card--back .lockup { left: 150px; top: 115px; }
  .card--back .lockup__role { color: var(--on-dark-soft); }
  .card--front .lockup { left: 110px; top: 48px; }
  .card--front .lockup__role { color: var(--ink-soft); }

  .addresses { position: absolute; left: 50px; bottom: 50px; list-style: none; }
  .addresses li {
    display: flex; align-items: center; gap: 10px;
    font-size: 15px; line-height: 28px; color: var(--on-dark);
  }
  .addresses svg { width: 12px; height: 16px; fill: var(--on-dark); flex: none; }

  .contacts { position: absolute; right: 42px; top: 132px; list-style: none; }
  .contacts li {
    display: flex; align-items: center; justify-content: flex-end; gap: 12px;
    font-size: 15px; line-height: 30px; color: var(--ink);
  }
  .contacts svg { width: 15px; height: 15px; fill: var(--ink); flex: none; }

  .divider {
    position: absolute; left: 0; right: 0; top: 232px;
    height: 2px; background: var(--ink);
  }
</style>
</head>
<body>
<main class="sheet">

  <section class="card card--back" aria-label="Verso">
    <div class="lockup">
      <span class="lockup__dot"></span>
      <div>
        <p class="lockup__name">Loïc Vermande</p>
        <p class="lockup__role">Massothérapeute / Préparateur Mental</p>
      </div>
    </div>
    <ul class="addresses">
      <li>
        <svg viewBox="0 0 12 16"><path d="M6 0a6 6 0 0 0-6 6c0 4.5 6 10 6 10s6-5.5 6-10a6 6 0 0 0-6-6zm0 8.3A2.3 2.3 0 1 1 6 3.7a2.3 2.3 0 0 1 0 4.6z"/></svg>
        Chemin des Ormelets 27B, 1400 Yverdon-les-Bains
      </li>
      <li>
        <svg viewBox="0 0 12 16"><path d="M6 0a6 6 0 0 0-6 6c0 4.5 6 10 6 10s6-5.5 6-10a6 6 0 0 0-6-6zm0 8.3A2.3 2.3 0 1 1 6 3.7a2.3 2.3 0 0 1 0 4.6z"/></svg>
        Rue des Tanneries 9, 1700 Freiburg
      </li>
    </ul>
  </section>

  <section class="card card--front" aria-label="Recto">
    <div class="lockup">
      <span class="lockup__dot"></span>
      <div>
        <p class="lockup__name">Loïc Vermande</p>
        <p class="lockup__role">Massothérapeute / Préparateur Mental</p>
      </div>
    </div>
    <ul class="contacts">
      <li>078 315 26 49
        <svg viewBox="0 0 16 16"><path d="M3.5 1l2.3 2.6-1.3 2a9 9 0 0 0 5.9 5.9l2-1.3 2.6 2.3-1.5 2.3C6.7 16.4-.4 9.3.9 2.5z"/></svg>
      </li>
      <li>info@loicvermande-exemple.ch
        <svg viewBox="0 0 16 16"><path d="M0 3h16v10H0zm1.5 1.2V5l6.5 4.2L14.5 5v-.8zm0 2.6v4.9h13V6.8L8 11z"/></svg>
      </li>
      <li>www.loicvermande-exemple.ch
        <svg viewBox="0 0 16 16"><path d="M8 0a8 8 0 1 0 0 16A8 8 0 0 0 8 0zm5.9 7.3h-2.5a12 12 0 0 0-1-4.9 6.5 6.5 0 0 1 3.5 4.9zM8 1.6c.8 1 1.7 3 1.9 5.7H6.1C6.3 4.6 7.2 2.6 8 1.6zM5.6 2.4a12 12 0 0 0-1 4.9H2.1a6.5 6.5 0 0 1 3.5-4.9zM2.1 8.7h2.5a12 12 0 0 0 1 4.9 6.5 6.5 0 0 1-3.5-4.9zM8 14.4c-.8-1-1.7-3-1.9-5.7h3.8c-.2 2.7-1.1 4.7-1.9 5.7zm2.4-.8a12 12 0 0 0 1-4.9h2.5a6.5 6.5 0 0 1-3.5 4.9z"/></svg>
      </li>
    </ul>
    <div class="divider"></div>
  </section>

</main>
</body>
</html>
```